Briarwood Homes Lakeshore Customer Brochure

Need a brochure designed that is clean and minimal that contains our logo, and contact information. Would like an area where we could insert business cards, and slips on both sides of the openings to place sheets of paper in. Would prefer to have the COVER LETTER I have attached printed on one side of the opening.

Target Market(s)

Home buyers

Font styles to use
Sans Serif

Colors

Designer to choose colors to be used in the design.

Requirements
Must have
• Logo, contact info, website, etc. Must be minimal in design and very clean looking.
Nice to have
• Please see above
Should not have
• No stock pictures of homes, builds, etc. Need it to look very clean

```html
<!DOCTYPE html>
<html lang="en">
<head>
<meta charset="utf-8">
<title>Briarwood Homes Lakeshore – Presentation Folder</title>
<link href="https://fonts.googleapis.com/css2?family=Roboto+Condensed:wght@700&display=swap" rel="stylesheet">
<style>
  :root {
    --backdrop: #565656;
    --paper: #ffffff;
    --pocket-tan: #d1a77b;
    --watermark-grey: #dcdcdc;
    --card-paper: #ffffff;
  }
  html, body {
    margin: 0;
    padding: 0;
    width: 1200px;
    height: 1200px;
    overflow: hidden;
    background: var(--backdrop);
  }
  .folder-spread {
    display: block;
    width: 1200px;
    height: 1200px;
  }
  .panel { fill: var(--paper); }
  .pocket { fill: var(--pocket-tan); }
  .pocket-rule {
    fill: none;
    stroke: var(--pocket-tan);
    stroke-width: 1.6;
  }
  .brand-name {
    font-family: "Roboto Condensed", "Arial Narrow", sans-serif;
    font-weight: 700;
    text-anchor: start;
  }
  .brand-name--faint { fill: var(--watermark-grey); }
  .brand-name--faint .brand-line-main { font-size: 31px; }
  .brand-name--faint .brand-line-sub { font-size: 17px; }
  .brand-mark--faint { fill: var(--watermark-grey); }
  .business-card { fill: var(--card-paper); }
  .brand-name--card { fill: var(--pocket-tan); }
  .brand-name--card .brand-line-main { font-size: 17px; }
  .brand-name--card .brand-line-sub { font-size: 10px; }
  .brand-mark--card { fill: var(--pocket-tan); }
</style>
</head>
<body>
<svg class="folder-spread" viewBox="0 0 1200 1200" xmlns="http://www.w3.org/2000/svg" aria-label="Briarwood Homes Lakeshore presentation folder, inside spread">
  <!-- inside panels -->
  <rect class="panel panel--left" x="36" y="140" width="564" height="804"/>
  <rect class="panel panel--right" x="600" y="140" width="564" height="804"/>

  <!-- pocket rules -->
  <polyline class="pocket-rule" points="36,838 320,790 600,840 883,790 1164,840"/>

  <!-- pockets -->
  <polygon class="pocket pocket--left" points="36,850 320,801 600,850 600,944 36,944"/>
  <polygon class="pocket pocket--right" points="600,850 883,801 1164,850 1164,944 600,944"/>

  <!-- faint brand names on panels -->
  <g class="panel-brand panel-brand--left">
    <rect class="brand-mark--faint" x="207" y="439" width="44" height="44"/>
    <text class="brand-name brand-name--faint">
      <tspan class="brand-line-main" x="264" y="462" textLength="166" lengthAdjust="spacingAndGlyphs">BRIARWOOD</tspan>
      <tspan class="brand-line-sub" x="290" y="484" textLength="116" lengthAdjust="spacing">HOMES</tspan>
    </text>
  </g>
  <g class="panel-brand panel-brand--right">
    <rect class="brand-mark--faint" x="771" y="439" width="44" height="44"/>
    <text class="brand-name brand-name--faint">
      <tspan class="brand-line-main" x="828" y="462" textLength="166" lengthAdjust="spacingAndGlyphs">BRIARWOOD</tspan>
      <tspan class="brand-line-sub" x="854" y="484" textLength="116" lengthAdjust="spacing">HOMES</tspan>
    </text>
  </g>

  <!-- business card in right pocket -->
  <g class="business-card-slot">
    <rect class="business-card" x="784" y="834" width="174" height="85"/>
    <rect class="brand-mark--card" x="808" y="864" width="24" height="25"/>
    <text class="brand-name brand-name--card">
      <tspan class="brand-line-main" x="839" y="877" textLength="95" lengthAdjust="spacingAndGlyphs">BRIARWOOD</tspan>
      <tspan class="brand-line-sub" x="854" y="890" textLength="66" lengthAdjust="spacing">HOMES</tspan>
    </text>
  </g>
</svg>
</body>
</html>
```